Poster Design October

We are a Poker Club (Harlow Bay Veterans Cardroom Club). We run poker tournaments three night a week in Mount Gambier
We require a poster to advertise our upcoming major Poker tournament
The details of the event are set out below
ANNUAL $200 BUY IN TOURNAMENT
OCTOBER LONG WEEK END
4-5 OCTOBER 2014
$100K STARTING STACK
45 MIN BLINDS
HARLOW BAY VETERANS LEAGUE
27 DELLWYN STREET
KELVERTON SA 5371
10:00AM START (SA TIME)
REGISTRATION 9:30AM (SA TIME)
EMAIL HBVCARDS@MAILNEST.COM.AU FOR MORE INFORMATION
FIND US ON FRIENDBOARD: HBV CARDS 2014
I have attached a flyer this is something like what we are looking for
I Have also attached the HBV logo which need to be included
Poker plyers 18+ both genders
Club

```html
<!DOCTYPE html>
<html lang="en">
<head>
<meta charset="utf-8">
<title>October Long Weekend Poker Tournament</title>
<link rel="stylesheet" href="https://fonts.googleapis.com/css2?family=Oswald:wght@500;600;700&family=Poiret+One&family=Russo+One&display=swap">
<style>
  :root {
    --felt-light: #3d6b2c;
    --felt-mid: #23461b;
    --felt-dark: #0e1d0b;
    --band: rgba(10, 12, 10, 0.82);
    --band-inner: #1a1c1c;
    --lime: #e4ef3c;
    --lime-soft: #cbd83a;
    --gold: #e9d57a;
    --suit-red: #e0222a;
    --white: #ffffff;
    --link-blue: #4a8fe0;
    --chip-core: #3a3c3e;
    --chip-rim: #1c1d1e;
    --chip-ring: #8a8c8e;
    --cards-light: #f4efef;
    --cards-tint: #e6d3d3;
  }
  * { box-sizing: border-box; margin: 0; padding: 0; }
  html, body { width: 790px; height: 1200px; overflow: hidden; background: #111; }
  .poster {
    position: relative;
    width: 790px;
    height: 1200px;
    overflow: hidden;
    background: radial-gradient(ellipse at 45% 40%, var(--felt-light) 0%, var(--felt-mid) 45%, var(--felt-dark) 100%);
    font-family: "Oswald", sans-serif;
  }

  /* corner peel */
  .corner-peel { position: absolute; top: 0; right: 0; width: 340px; height: 330px; }

  /* chips: plain round discs carrying text */
  .chip {
    position: absolute;
    border-radius: 50%;
    background: radial-gradient(circle at 50% 45%, var(--chip-core) 0%, var(--chip-rim) 100%);
    box-shadow: inset 0 0 0 4px var(--chip-ring), 0 4px 14px rgba(0, 0, 0, 0.55);
    display: flex; flex-direction: column; align-items: center; justify-content: center;
    color: var(--gold); font-family: "Oswald", sans-serif; font-weight: 700;
    text-align: center; line-height: 1.05;
  }
  .chip-annual { left: 44px; top: 74px; width: 240px; height: 240px; font-size: 34px; }
  .chip-stack { left: 570px; top: 794px; width: 172px; height: 172px; font-size: 20px; }
  .chip-stack .chip-big { font-size: 27px; }
  .chip-stack .chip-mid { font-size: 22px; }

  .band {
    position: absolute; left: 0; width: 790px;
    background: var(--band);
    display: flex; align-items: center; justify-content: center;
    font-family: "Poiret One", sans-serif; font-weight: 400;
  }
  .band-weekend { top: 374px; height: 56px; font-size: 50px; gap: 10px; }
  .band-weekend .accent { color: var(--lime); font-weight: 700; letter-spacing: 1px; }
  .band-weekend .soft { color: var(--lime-soft); letter-spacing: 2px; }
  .suit { font-family: sans-serif; font-size: 40px; }
  .suit-red { color: var(--suit-red); }
  .suit-dark { color: #111; -webkit-text-stroke: 1.5px #ddd; }

  .band-title {
    top: 439px; height: 257px;
    flex-direction: column;
    background: linear-gradient(180deg, #2a2c2d 0%, var(--band-inner) 50%, #262829 100%);
    border-top: 2px solid #050505; border-bottom: 2px solid #050505;
    font-family: "Russo One", sans-serif;
  }
  .title-line {
    line-height: 1;
    font-weight: 400;
    background: linear-gradient(90deg, #f2f23a 0%, #8fe24a 30%, #e6332a 48%, #ffffff 62%, #9be852 78%, #3fd6a8 100%);
    -webkit-background-clip: text; background-clip: text;
    color: transparent;
  }
  .title-poker { font-size: 104px; letter-spacing: 2px; }
  .title-tournament { font-size: 108px; letter-spacing: -2px; margin-top: 4px; }

  .band-date { top: 702px; height: 66px; font-size: 62px; color: var(--lime); justify-content: space-between; padding: 0 22px; }
  .band-date .date-text { font-weight: 700; letter-spacing: 3px; }
  .band-date .suit { font-size: 56px; }

  .schedule {
    position: absolute; left: 0; top: 869px; width: 462px; height: 105px;
    background: rgba(10, 12, 10, 0.72);
    padding: 12px 0 0 10px;
    font-family: "Poiret One", sans-serif;
    color: var(--lime); font-size: 28px; line-height: 42px;
  }
  .schedule strong { font-weight: 700; }

  .venue-mark {
    position: absolute; left: 104px; top: 1004px; width: 116px; height: 116px;
    border: 4px solid var(--white); border-radius: 50%;
    display: flex; align-items: center; justify-content: center;
    color: var(--white); font-weight: 700; font-size: 34px;
  }
  .venue-address {
    position: absolute; left: 222px; top: 1022px; width: 360px;
    text-align: center; color: var(--white); font-style: normal;
    font-weight: 600; font-size: 24px; line-height: 31px;
  }
  .contact-line {
    position: absolute; left: 0; top: 1162px; width: 790px; text-align: center;
    color: var(--white); font-weight: 600; font-size: 17px; letter-spacing: 0.2px;
  }
  .contact-line .link { color: var(--link-blue); }
</style>
</head>
<body>
<main class="poster">

  <svg class="corner-peel" viewBox="0 0 340 330" role="img" aria-label="Scattered playing cards revealed beneath a peeled-back corner">
    <defs>
      <linearGradient id="cards-tone" x1="0" y1="0" x2="1" y2="1">
        <stop offset="0" stop-color="var(--cards-light)"/>
        <stop offset="1" stop-color="var(--cards-tint)"/>
      </linearGradient>
      <linearGradient id="peel-tone" x1="0" y1="0" x2="1" y2="1">
        <stop offset="0" stop-color="#8f8f8f"/>
        <stop offset="0.55" stop-color="#ffffff"/>
        <stop offset="1" stop-color="#c9c9c9"/>
      </linearGradient>
    </defs>
    <path d="M70 0 H340 V318 C280 262 200 170 140 100 C110 65 85 30 70 0 Z" fill="url(#cards-tone)"/>
    <path d="M0 0 H70 C85 30 110 65 140 100 C200 170 280 262 340 318 V330 C250 270 130 170 85 110 C45 60 15 25 0 0 Z" fill="url(#peel-tone)"/>
  </svg>

  <div class="chip chip-annual">
    <span>ANNUAL</span><span>$200 BUY IN</span><span>TOURNAMENT</span>
  </div>

  <div class="band band-weekend">
    <span class="suit suit-red">♦</span>
    <span class="accent">OCTOBER</span>
    <span class="soft">LONG WEEKEND</span>
    <span class="suit suit-dark">♣</span>
  </div>

  <div class="band band-title">
    <h1 class="title-line title-poker">POKER</h1>
    <div class="title-line title-tournament">TOURNAMENT</div>
  </div>

  <div class="band band-date">
    <span class="suit suit-dark">♠</span>
    <span class="date-text">4-5 OCTOBER 2014</span>
    <span class="suit suit-red">♥</span>
  </div>

  <div class="chip chip-stack">
    <span class="chip-mid">$100K</span><span>STARTING STACK</span><span class="chip-big">45 MIN</span><span class="chip-mid">BLINDS</span>
  </div>

  <div class="schedule">
    <div>✦ <strong>10:00AM START (SA TIME)</strong></div>
    <div>✦ <strong>REGISTRATION 9:30AM (SA TIME)</strong></div>
  </div>

  <div class="venue-mark">HBV</div>

  <address class="venue-address">
    HARLOW BAY VETERANS LEAGUE<br>
    27 DELLWYN STREET<br>
    KELVERTON SA 5371
  </address>

  <p class="contact-line">
    EMAIL <span class="link">HBVCARDS@MAILNEST.COM.AU</span> FOR MORE INFORMATION * FIND US ON FRIENDBOARD: <span class="link">HBV CARDS 2014</span>
  </p>

</main>
</body>
</html>
```